Car Rental Web Site. Design the main page, win contest and continue working with us on this site in a project environment at $50-100 per page.

WE WANT ONLY THE BEST!
We will be working on front and back end of the Car Rental website.
Design 1 page of the website for this contest, be a winner and continue later on a rest of the website on a separate project that we will open on this platform and earn USD50-100 per designed page (depending on difficulty).

You are required to prepare a running prototype of 1 main page of a Car Rental Website. We have pretty much drawn the idea, but you need to design it really modern looking using Bootstrap and be creative with animations. We want unique designs, so think twice if you are planning to use any templates.

Please use the color gamma and corporate style of [login to view URL] and be free to innovate and make a user friendly travel shopping experience.

Websites that we like:
You can look at these great web sites for inspiration while doing your work:
[login to view URL] - great looking design put together in one place. It pretty much uses our color gamma and we absolutely love it.
[login to view URL] - the way they do buttons is really nice.

Please refer to the attached sketch to see the details of the landing.
Technology required (ONLY USE AS PROVIDED): HTML5, CSS, Bootstrap, jQuery, JSON.
Requirements: Fully responsive for all devices and browsers!

```html
<!DOCTYPE html>
<html lang="en">
<head>
<meta charset="utf-8">
<title>Car Rental Malaysia</title>
<link rel="stylesheet" href="https://fonts.googleapis.com/css2?family=Roboto:wght@300;400;500;700&display=swap">
<style>
:root{
  --pink:#d4096d;
  --pink-dark:#b5075c;
  --ink:#2b2b2b;
  --grey-band:#ededed;
  --grey-soft:#f3f3f3;
  --caption:#4a4a4a;
  --footer:#333333;
  --footer-text:#9a9a9a;
  --line:#cfcfcf;
  --white:#ffffff;
}
*{box-sizing:border-box;margin:0;padding:0}
html,body{width:1200px;height:2833px;overflow:hidden;background:var(--white);font-family:"Roboto",Arial,sans-serif;color:var(--ink)}
.page{position:relative;width:1200px;height:2833px}

/* header */
.site-header{position:absolute;top:0;left:0;width:1200px;height:78px;background:var(--pink);color:var(--white)}
.brand{position:absolute;left:0;top:0;height:78px;width:372px;background:var(--pink-dark);clip-path:polygon(0 0,100% 0,93% 100%,0 100%);display:flex;align-items:center;padding-left:59px;font-size:29px;font-weight:700;letter-spacing:.3px}
.main-nav{position:absolute;left:413px;top:27px;display:flex;gap:47px;font-size:17px}
.util{position:absolute;right:59px;top:12px;text-align:right;font-size:11px}
.util-row{display:flex;align-items:center;gap:18px;margin-top:6px;font-size:18px}
.util-row .login{font-size:14px;display:flex;align-items:center;gap:5px}
.util-row .phone{display:flex;align-items:center;gap:5px}

/* hero */
.hero{position:absolute;top:78px;left:0;width:1200px;height:522px;background:linear-gradient(180deg,#6f6a52 0%,#3d3a30 45%,#29292a 100%)}
.hero-photo{position:absolute;inset:0;background:radial-gradient(ellipse 420px 300px at 560px 200px,#1b1c1e 0%,#1b1c1e 55%,transparent 70%),linear-gradient(90deg,#8a7a47 0%,#5c5a40 40%,#6d6a4c 100%)}
.hero-title{position:absolute;top:273px;left:0;width:1200px;text-align:center;color:var(--white);font-size:36px;font-weight:700;letter-spacing:-.3px;text-shadow:0 2px 4px rgba(0,0,0,.5)}
.hero-sub{position:absolute;top:320px;left:0;width:1200px;text-align:center;color:var(--white);font-size:20px;font-weight:500}
.hero-shade{position:absolute;left:0;top:371px;width:1200px;height:151px;background:rgba(40,40,40,.72)}
.hero-tabs{position:absolute;top:363px;left:0;width:1200px;height:42px;display:flex;justify-content:center}
.hero-tabs::before{content:"";position:absolute;left:365px;right:365px;top:21px;border-top:1px solid rgba(255,255,255,.5)}
.hero-tab{position:relative;height:42px;display:flex;align-items:center;justify-content:center;font-size:16px}
.hero-tab-car{width:131px;background:#5a5a5a;color:#eee}
.hero-tab-travel{width:165px;background:var(--white);color:var(--ink)}
.booking{position:absolute;top:429px;left:60px;width:1080px;color:var(--white);font-size:14px}
.field-label{position:absolute;top:0}
.field{position:absolute;top:27px;height:39px;background:var(--white);border:1px solid #ddd;color:#666;font-size:12px;display:flex;align-items:center;padding-left:10px}
.submit{position:absolute;top:27px;left:855px;width:226px;height:39px;background:var(--pink);color:var(--white);font-size:16px;font-weight:500;display:flex;align-items:center;justify-content:center}

/* section heading tab */
.section-band{position:absolute;left:0;width:1200px;background:var(--grey-band)}
.section-tab{position:absolute;left:429px;width:342px;height:100%;background:var(--pink);clip-path:polygon(0 0,100% 0,92% 100%,8% 100%);color:var(--white);font-size:24px;display:flex;align-items:center;justify-content:center}

/* fleet */
.fleet{position:absolute;top:680px;left:60px;width:1080px;height:240px}
.fleet-card{position:absolute;top:0;height:240px;border:1px solid var(--line);background:var(--white)}
.fleet-photo{position:absolute;left:10px;right:10px;top:14px;height:170px;background:radial-gradient(ellipse 45% 38% at 50% 55%,#b8bcc2 0%,#dfe1e4 70%,#fff 100%)}
.fleet-photo.blue{background:radial-gradient(ellipse 45% 38% at 50% 55%,#3a86c8 0%,#bcd6ec 72%,#fff 100%)}
.fleet-caption{position:absolute;left:0;right:0;bottom:0;height:41px;background:var(--caption);color:var(--white);font-size:16px;display:flex;align-items:center;justify-content:space-between;padding:0 16px}

/* stats */
.stats{position:absolute;top:940px;left:0;width:1200px;height:144px;background:var(--grey-soft)}
.stat-left{position:absolute;left:0;top:0;width:640px;height:144px;background:#e6e6e6}
.stat{position:absolute;top:0;height:144px;display:flex;align-items:center;font-size:18px;line-height:1.45}
.stat .sep{width:1px;height:64px;background:var(--line);margin:0 20px}
.badge-label{font-size:9px;color:var(--pink);text-align:center;line-height:1.1}

/* services */
.services-head{position:absolute;top:1105px;left:0;width:1200px;height:59px;background:var(--pink);color:var(--white);font-size:24px;display:flex;align-items:center;justify-content:center}
.service{position:absolute;top:1196px;width:260px;text-align:center}
.service-ring{width:212px;height:212px;margin:0 auto;border-radius:50%;border:4px solid var(--pink);display:flex;align-items:center;justify-content:center;background:var(--white);box-shadow:inset 0 0 0 10px #fff,inset 0 0 0 11px #eee}
.service-btn{margin-top:25px;width:260px;height:41px;border:1px solid var(--line);font-size:18px;display:flex;align-items:center;justify-content:space-between;padding:0 14px}
.service-divider{position:absolute;top:1210px;height:268px;border-left:1px dotted #bbb}

/* packages */
.package{position:absolute;top:1620px;width:323px}
.package-card{height:260px;border:1px solid var(--line);position:relative;background:var(--white)}
.package-photo{position:absolute;left:20px;right:20px;top:20px;height:120px;background:linear-gradient(90deg,#c9ccd1 0%,#e8e9eb 60%,#fff 70%,#d8c8c0 100%)}
.package-rule{position:absolute;left:0;right:0;top:159px;height:16px}
.package-text{position:absolute;top:187px;left:28px;right:28px;text-align:center;font-size:18px;line-height:1.35}
.package-actions{margin-top:5px;height:41px;border:1px solid var(--pink);display:flex;font-size:18px}
.package-actions .all{width:92px;border-right:1px solid var(--pink);display:flex;align-items:center;justify-content:center;color:var(--ink)}
.package-actions .book{flex:1;display:flex;align-items:center;justify-content:space-between;padding:0 10px;color:var(--pink);font-weight:500}

/* travel + map */
.travel-photo{position:absolute;top:1973px;left:0;width:577px;height:487px;background:linear-gradient(160deg,#6c6a66 0%,#5a4a3a 50%,#3f342b 100%)}
.travel-title{position:absolute;left:68px;top:36px;color:var(--white);font-size:38px;font-weight:700;line-height:1}
.travel-title span{display:block;font-size:33px}
.map{position:absolute;top:1973px;left:577px;width:623px;height:487px;background:linear-gradient(135deg,#e8ead8 0%,#dfe8cf 50%,#cfe3bd 100%)}

/* partners */
.partners-title{position:absolute;top:2493px;left:0;width:1200px;text-align:center;font-size:19px}
.partners{position:absolute;top:2530px;left:45px;width:1110px;display:flex;justify-content:space-between;align-items:center}
.partner{background:#c4c4c4}

/* footer */
.site-footer{position:absolute;top:2631px;left:0;width:1200px;height:202px;background:var(--footer);color:var(--footer-text);text-align:center}
.footer-links{margin-top:55px;display:flex;justify-content:center;gap:30px;font-size:13px}
.copyright{margin-top:18px;font-size:13px}
.social{margin-top:16px;display:flex;justify-content:center;gap:8px}
.social span{width:27px;height:27px;border-radius:50%;background:#666}
.social span:first-child{background:var(--pink)}
</style>
</head>
<body>
<div class="page">

  <header class="site-header">
    <div class="brand">LOGO GOES HERE</div>
    <nav class="main-nav"><span>Out Fleet</span><span>Leasing</span><span>Rental Offers</span><span>Contact us</span></nav>
    <div class="util">
      <div>EN &nbsp;|&nbsp; USD</div>
      <div class="util-row">
        <span class="login"><svg width="13" height="14" viewBox="0 0 13 14"><circle cx="6.5" cy="4" r="3.2" fill="#fff"/><path d="M0.5 14c0-4 2.5-6 6-6s6 2 6 6z" fill="#fff"/></svg>LOGIN</span>
        <span class="phone"><svg width="14" height="18" viewBox="0 0 14 18"><path d="M3 1l3 3-2 2c1 3 3 6 5 7l2-2 3 3-3 3C5 16 0 9 0 4z" fill="#fff"/></svg>+60 1200 555 014</span>
      </div>
    </div>
  </header>

  <section class="hero">
    <div class="hero-photo" role="img" aria-label="Photo of a dark SUV on a country road with autumn trees"></div>
    <div class="hero-shade"></div>
    <h1 class="hero-title">BEST PRICED CAR RENTAL IN MALAYSIA</h1>
    <p class="hero-sub">AT YOUR FINGERTIPS.....</p>
    <div class="hero-tabs"><div class="hero-tab hero-tab-car">Car Rental</div><div class="hero-tab hero-tab-travel">Travel Packages</div></div>
    <form class="booking">
      <span class="field-label" style="left:0">Date&amp; time</span>
      <span class="field-label" style="left:285px">Drop Off Date &amp; Time</span>
      <span class="field-label" style="left:569px">Pick up location</span>
      <div class="field" style="left:0;width:92px">20.11.2016</div>
      <div class="field" style="left:92px;width:186px">10.00</div>
      <div class="field" style="left:285px;width:278px"></div>
      <div class="field" style="left:569px;width:279px;justify-content:flex-end;padding-right:20px">
        <svg width="14" height="9" viewBox="0 0 14 9"><path d="M1 1l6 6 6-6" stroke="#222" stroke-width="2.5" fill="none"/></svg>
      </div>
      <div class="submit">SUBMIT</div>
    </form>
  </section>

  <div class="section-band" style="top:623px;height:48px"><div class="section-tab">Our Car Rental Fleet</div></div>

  <section class="fleet">
    <div class="fleet-card" style="left:0;width:256px"><div class="fleet-photo" role="img" aria-label="White compact sedan"></div><div class="fleet-caption">Corvane Attra<svg width="20" height="20" viewBox="0 0 20 20"><circle cx="10" cy="10" r="8" stroke="#fff" stroke-width="1.5" fill="none"/><path d="M8 6l4 4-4 4" stroke="#fff" stroke-width="1.5" fill="none"/></svg></div></div>
    <div class="fleet-card" style="left:265px;width:264px"><div class="fleet-photo" role="img" aria-label="Silver passenger van"></div><div class="fleet-caption">Halden Stellar<svg width="20" height="20" viewBox="0 0 20 20"><circle cx="10" cy="10" r="8" stroke="#fff" stroke-width="1.5" fill="none"/><path d="M8 6l4 4-4 4" stroke="#fff" stroke-width="1.5" fill="none"/></svg></div></div>
    <div class="fleet-card" style="left:539px;width:265px"><div class="fleet-photo" role="img" aria-label="Silver executive sedan"></div><div class="fleet-caption">Varenta Executive<svg width="20" height="20" viewBox="0 0 20 20"><circle cx="10" cy="10" r="8" stroke="#fff" stroke-width="1.5" fill="none"/><path d="M8 6l4 4-4 4" stroke="#fff" stroke-width="1.5" fill="none"/></svg></div></div>
    <div class="fleet-card" style="left:813px;width:266px"><div class="fleet-photo blue" role="img" aria-label="Blue family sedan"></div><div class="fleet-caption">Pronta Sagi<svg width="20" height="20" viewBox="0 0 20 20"><circle cx="10" cy="10" r="8" stroke="#fff" stroke-width="1.5" fill="none"/><path d="M8 6l4 4-4 4" stroke="#fff" stroke-width="1.5" fill="none"/></svg></div></div>
  </section>

  <section class="stats">
    <div class="stat-left"></div>
    <div class="stat" style="left:66px">
      <div>
        <svg width="68" height="40" viewBox="0 0 68 40"><circle cx="34" cy="18" r="15" fill="none" stroke="#d4096d" stroke-width="3"/><path d="M27 20l5 5 10-11" stroke="#d4096d" stroke-width="3" fill="none"/><path d="M6 30c4-6 4-14 10-20M62 30c-4-6-4-14-10-20" stroke="#d4096d" stroke-width="3" fill="none"/></svg>
        <div class="badge-label">11 Year<br>Experienced</div>
      </div>
      <span class="sep"></span>
      <span>11 years Experienced Licenced Tour &nbsp;Operator<br>in Malaysia &amp; Singapur</span>
    </div>
    <div class="stat" style="left:718px">
      <svg width="82" height="50" viewBox="0 0 82 50"><circle cx="22" cy="14" r="9" fill="#d4096d"/><circle cx="40" cy="12" r="9" fill="#d4096d"/><path d="M6 42c0-12 8-18 16-18s16 6 16 18z" fill="#d4096d"/><path d="M26 40c0-12 7-18 14-18s14 6 14 18z" fill="#d4096d"/><path d="M58 44V28h6l4-12c4 0 5 3 4 8h8v20z" fill="#d4096d"/></svg>
      <span class="sep"></span>
      <span>24845 &nbsp;Satisfied Customers</span>
    </div>
  </section>

  <div class="services-head">Our Car Rental Services in Kuala Lumpur</div>

  <div class="service" style="left:83px">
    <div class="service-ring">
      <svg width="90" height="104" viewBox="0 0 90 104"><g fill="none" stroke="#d4096d" stroke-width="4"><circle cx="16" cy="16" r="10"/><path d="M26 16h44M60 16v8M68 16v6"/><path d="M10 60l8-18h54l8 18v26H10z"/><path d="M10 60h70"/><circle cx="24" cy="72" r="5"/><circle cx="66" cy="72" r="5"/><path d="M16 86v10h12V86M62 86v10h12V86"/></g></svg>
    </div>
    <div class="service-btn">Hire &amp; Drive<svg width="20" height="20" viewBox="0 0 20 20"><circle cx="10" cy="10" r="8" stroke="#333" stroke-width="1.5" fill="none"/><path d="M8 6l4 4-4 4" stroke="#333" stroke-width="1.5" fill="none"/></svg></div>
  </div>
  <div class="service-divider" style="left:409px"></div>
  <div class="service" style="left:470px">
    <div class="service-ring">
      <svg width="110" height="100" viewBox="0 0 110 100"><path d="M22 8h36l-4 14H26z" fill="#d4096d"/><rect x="26" y="24" width="28" height="22" rx="10" fill="#d4096d"/><path d="M6 96V64c0-8 6-14 14-14h40c8 0 14 6 14 14v32z" fill="#d4096d"/><path d="M40 52l-4 44h8z" fill="#fff"/><path d="M70 40h32l6 20v20H70z" fill="#d4096d"/><circle cx="96" cy="66" r="4" fill="#fff"/></svg>
    </div>
    <div class="service-btn">Driven<svg width="20" height="20" viewBox="0 0 20 20"><circle cx="10" cy="10" r="8" stroke="#333" stroke-width="1.5" fill="none"/><path d="M8 6l4 4-4 4" stroke="#333" stroke-width="1.5" fill="none"/></svg></div>
  </div>
  <div class="service-divider" style="left:804px"></div>
  <div class="service" style="left:880px">
    <div class="service-ring">
      <svg width="120" height="90" viewBox="0 0 120 90"><path d="M32 44l8-26h44l8 26v18H32z" fill="#d4096d"/><circle cx="44" cy="48" r="5" fill="#fff"/><circle cx="80" cy="48" r="5" fill="#fff"/><path d="M4 66h30c8 0 14 4 18 6h26l30-14c6-2 10 4 4 8L76 86H4z" fill="#d4096d"/></svg>
    </div>
    <div class="service-btn">Long term lease<svg width="20" height="20" viewBox="0 0 20 20"><circle cx="10" cy="10" r="8" stroke="#333" stroke-width="1.5" fill="none"/><path d="M8 6l4 4-4 4" stroke="#333" stroke-width="1.5" fill="none"/></svg></div>
  </div>

  <div class="section-band" style="top:1523px;height:50px"><div class="section-tab" style="left:410px;width:380px">Try Our Rental Packages</div></div>

  <div class="package" style="left:60px">
    <div class="package-card"><div class="package-photo" role="img" aria-label="Silver van plus executive pen"></div>
      <svg class="package-rule" viewBox="0 0 323 16" preserveAspectRatio="none"><path d="M0 0h323v8H186l-24 8-24-8H0z" fill="#d4096d"/></svg>
      <p class="package-text">Book 2 Days &amp; Get an exclusive Pen worth RM 150</p></div>
    <div class="package-actions"><span class="all">ALL CAR</span><span class="book">BOOK NOW<svg width="20" height="20" viewBox="0 0 20 20"><circle cx="10" cy="10" r="8" stroke="#d4096d" stroke-width="1.5" fill="none"/><path d="M8 6l4 4-4 4" stroke="#d4096d" stroke-width="1.5" fill="none"/></svg></span></div>
  </div>
  <div class="package" style="left:439px">
    <div class="package-card"><div class="package-photo" role="img" aria-label="Silver van plus executive pen"></div>
      <svg class="package-rule" viewBox="0 0 323 16" preserveAspectRatio="none"><path d="M0 0h323v8H186l-24 8-24-8H0z" fill="#d4096d"/></svg>
      <p class="package-text">Pay 7 days Drive 8 + Executive Pen worth RM 150</p></div>
    <div class="package-actions"><span class="all">ALL CAR</span><span class="book">BOOK NOW<svg width="20" height="20" viewBox="0 0 20 20"><circle cx="10" cy="10" r="8" stroke="#d4096d" stroke-width="1.5" fill="none"/><path d="M8 6l4 4-4 4" stroke="#d4096d" stroke-width="1.5" fill="none"/></svg></span></div>
  </div>
  <div class="package" style="left:816px">
    <div class="package-card"><div class="package-photo" role="img" aria-label="Silver van plus executive pen"></div>
      <svg class="package-rule" viewBox="0 0 323 16" preserveAspectRatio="none"><path d="M0 0h323v8H186l-24 8-24-8H0z" fill="#d4096d"/></svg>
      <p class="package-text">Pay 10 Days Drive 12 days + Executive Pen woerth 150</p></div>
    <div class="package-actions"><span class="all">ALL CAR</span><span class="book">BOOK NOW<svg width="20" height="20" viewBox="0 0 20 20"><circle cx="10" cy="10" r="8" stroke="#d4096d" stroke-width="1.5" fill="none"/><path d="M8 6l4 4-4 4" stroke="#d4096d" stroke-width="1.5" fill="none"/></svg></span></div>
  </div>

  <section class="travel-photo" role="img" aria-label="Photo of a happy couple leaning out of a car window">
    <h2 class="travel-title">The Comfortable Way to<span>Travel in your own phase</span></h2>
  </section>
  <div class="map" role="img" aria-label="Road map of central Malaysia with rental pick-up points marked"></div>

  <p class="partners-title">Partner with us:</p>
  <div class="partners">
    <span class="partner" style="width:136px;height:64px;border-radius:32px"></span>
    <span class="partner" style="width:64px;height:64px;border-radius:50%"></span>
    <span class="partner" style="width:120px;height:64px;border-radius:50%"></span>
    <span class="partner" style="width:70px;height:70px;border-radius:50%"></span>
    <span class="partner" style="width:130px;height:64px;border-radius:32px"></span>
    <span class="partner" style="width:64px;height:64px;border-radius:50%"></span>
    <span class="partner" style="width:112px;height:64px;border-radius:50%"></span>
  </div>

  <footer class="site-footer">
    <div class="footer-links"><span>Contact Us</span><span>|</span><span>About Us</span><span>|</span><span>Privacy</span><span>|</span><span>Faq</span></div>
    <p class="copyright">COPYRIGHTS © 2016 Car rental ALL RIGHTS RESERVED</p>
    <div class="social"><span></span><span></span><span></span><span></span><span></span><span></span></div>
  </footer>

</div>
</body>
</html>
```